Need Bus charter business website,

I am starting a bus charter business in the near future. I am based in Geelong, Victoria in Australia. I will have a 25 or 28 seater bus that will be used to take people on charted trips. Whether they be to birthday parties, weddings, sporting events, corporate events, mystery trips, going down the Great Ocean Road, or anywhere someone wants. As for colour scheme, I'm leaning towards something blue and grey, but open to anything really that catches my eye. I played around with a basic web design program and made a basic site which I uploaded ( www.kelmoride.com.au) It has things which I wanted to include such as, services I will provide, trip information, contact form etc.

I don't mind if the layout is completely different to my site as it was only a template that was included in the program I used. I would like the overall design to be relatively fluid, not having to back-track a lot to navigate the site.

```html
<!DOCTYPE html>
<html lang="en">
<head>
<meta charset="utf-8">
<title>Kelmo Bus Tours</title>
<link rel="stylesheet" href="https://fonts.googleapis.com/css2?family=Roboto+Slab:wght@700&family=Roboto:wght@300;400&display=swap">
<style>
  :root {
    --nav-blue: #4dabf2;
    --nav-edge: #7cc2f6;
    --page-grey: #e6e6e6;
    --panel-white: #ffffff;
    --text-dark: #111111;
    --text-light: #ffffff;
    --hero-deep: #0d3f66;
    --hero-mid: #1f6fa6;
    --hero-light: #3d8fc4;
  }
  * { margin: 0; padding: 0; box-sizing: border-box; }
  html, body {
    width: 1200px;
    height: 579px;
    overflow: hidden;
    background: var(--page-grey);
  }
  body { position: relative; }
  .site-header {
    position: absolute;
    top: 0; left: 0;
    width: 1200px;
    height: 48px;
    background: var(--nav-blue);
    border-top: 2px solid var(--nav-edge);
    z-index: 2;
  }
  .brand {
    position: absolute;
    left: 65px;
    top: 8px;
    font-family: "Roboto Slab", "Rockwell", serif;
    font-weight: 700;
    font-size: 26px;
    line-height: 32px;
    color: var(--text-light);
    letter-spacing: -0.3px;
    white-space: nowrap;
  }
  .main-nav a {
    position: absolute;
    top: 13px;
    width: 140px;
    margin-left: -70px;
    text-align: center;
    font-family: "Roboto", sans-serif;
    font-weight: 300;
    font-size: 19px;
    line-height: 24px;
    color: var(--text-light);
    text-decoration: none;
  }
  .content-panel {
    position: absolute;
    left: 124px;
    top: 48px;
    width: 951px;
    height: 531px;
    overflow: hidden;
    background: var(--panel-white);
  }
  .hero {
    position: absolute;
    left: 104px;
    top: 35px;
    width: 762px;
    height: 285px;
    background:
      radial-gradient(ellipse at 85% 10%, #6fb6e6 0%, transparent 35%),
      linear-gradient(100deg, var(--hero-mid) 0%, var(--hero-light) 35%, var(--hero-deep) 60%, var(--hero-mid) 100%);
    box-shadow: 0 2px 6px rgba(0,0,0,0.45);
  }
  .intro-block {
    position: absolute;
    top: 384px;
    width: 385px;
    font-family: "Roboto", sans-serif;
    color: var(--text-dark);
  }
  .intro-block h2 {
    font-family: "Roboto Slab", "Rockwell", serif;
    font-weight: 700;
    font-size: 33px;
    line-height: 44px;
    text-align: center;
    padding-right: 10px;
    white-space: nowrap;
  }
  .intro-block p {
    margin-top: 5px;
    font-size: 24px;
    line-height: 32px;
    font-weight: 400;
  }
  .intro-welcome { left: 93px; }
  .intro-booking { left: 478px; }
</style>
</head>
<body>
  <header class="site-header">
    <div class="brand">Kelmo Bus Tours</div>
    <nav class="main-nav">
      <a href="#" style="left:377px">Home</a>
      <a href="#" style="left:524px">Services</a>
      <a href="#" style="left:670px">Book a Trip</a>
      <a href="#" style="left:817px">Offers</a>
      <a href="#" style="left:964px">About Us</a>
      <a href="#" style="left:1110px">Contact</a>
    </nav>
  </header>

  <main class="content-panel">
    <div class="hero" role="img" aria-label="Banner illustration for mystery tours"></div>

    <section class="intro-block intro-welcome">
      <h2>Welcome</h2>
      <p>We are an accredited bus company that operates bus trip and charter work in the Geelong area. We offer trips and charters for every occasion.</p>
    </section>

    <section class="intro-block intro-booking">
      <h2>Want to book a trip?</h2>
      <p>We are an accredited bus company that operates bus trip and charter work in the Geelong area. We offer trips and charters for every occasion.</p>
    </section>
  </main>
</body>
</html>
```